Stationary design for IT Consultancy
Stationary Design (Business Cards - Letter Heads - Envelopes - Presentation Folders - Power Point)
Stationary design for IT Consultancy - Information Technology
Creative Brief
Use standard fonts
Optional fonts can be used
Professional
Dean Marlow
Technical Director
14 Brindle Works Oakfield Lane Stoneham Wexshire WX7 2QP
dean.marlow@pivotal-nsg.net
www.pivotal-nsg.net

```html
<!DOCTYPE html>
<html lang="en">
<head>
<meta charset="utf-8">
<title>Pivotal Network Services Group – Stationery</title>
<link href="https://fonts.googleapis.com/css2?family=Open+Sans:wght@400;600;700&display=swap" rel="stylesheet">
<style>
  :root{
    --bg:#e9e9e9;
    --paper:#ffffff;
    --brand:#2f3f9e;
    --brand-dark:#1f2c78;
    --brand-soft:#c9cfee;
    --ink:#333a4a;
    --muted:#8a90a3;
    --card-dark:#3a3f4b;
  }
  *{box-sizing:border-box;margin:0;padding:0}
  html,body{width:1200px;height:937px;overflow:hidden}
  body{background:var(--bg);font-family:"Open Sans",Arial,sans-serif;color:var(--ink);position:relative}
  .sheet{position:absolute;background:var(--paper);box-shadow:0 3px 10px rgba(0,0,0,.25);overflow:hidden}
  .brand{display:flex;align-items:center;gap:6px;color:var(--brand);font-weight:700;letter-spacing:.08em;text-transform:uppercase}
  .brand-dot{border-radius:50%;background:var(--brand);flex:none}
  .brand-tag{display:block;font-weight:600;letter-spacing:.18em}
  .band{position:absolute;left:0;right:0;bottom:0;background:linear-gradient(90deg,#fff 0%,var(--brand-soft) 35%,var(--brand) 80%,var(--brand-dark) 100%)}
  .url{position:absolute;color:#fff;font-weight:600}
  .small{font-size:6px;line-height:1.45}

  /* letterhead */
  .letterhead{left:311px;top:233px;width:357px;height:455px}
  .letterhead .brand{position:absolute;left:16px;top:20px;font-size:21px}
  .letterhead .brand-dot{width:22px;height:22px}
  .letterhead .brand-tag{font-size:6.5px;margin-top:-2px}
  .letterhead .address{position:absolute;left:208px;top:20px;font-size:5.5px;line-height:1.5;color:var(--ink)}
  .letterhead .watermark{position:absolute;left:72px;top:150px;width:200px;height:200px;border-radius:50%;background:radial-gradient(circle,#eef0fa 0%,#dfe3f5 70%,transparent 71%)}
  .letterhead .band{height:46px;background:linear-gradient(180deg,#fff 0%,#e7e9f6 40%,var(--brand) 100%)}
  .letterhead .url{left:14px;bottom:14px;font-size:6px;color:#fff}
  .letterhead .corner-dot{position:absolute;right:16px;bottom:12px;width:18px;height:18px;border-radius:50%;background:#fff;opacity:.85}

  /* envelope front */
  .envelope-front{left:721px;top:233px;width:418px;height:190px}
  .envelope-front .brand{position:absolute;left:14px;top:12px;font-size:15px}
  .envelope-front .brand-dot{width:16px;height:16px}
  .envelope-front .brand-tag{font-size:5px}
  .envelope-front .address{position:absolute;left:14px;top:44px;font-size:5.5px;line-height:1.5}
  .envelope-front .band{height:42px;background:linear-gradient(180deg,#fff 0%,#e3e6f6 35%,var(--brand) 100%)}
  .envelope-front .url{left:14px;bottom:16px;font-size:6px}
  .envelope-front .corner-dot{position:absolute;right:16px;bottom:14px;width:16px;height:16px;border-radius:50%;background:#fff;opacity:.85}

  /* envelope back */
  .envelope-back{left:721px;top:511px;width:418px;height:177px}
  .envelope-back svg{position:absolute;left:0;top:0}
  .envelope-back .flap-dot{position:absolute;left:199px;top:40px;width:20px;height:20px;border-radius:50%;border:2px solid #fff}

  /* business cards */
  .card{left:68px;width:185px}
  .card .name{font-size:7.5px;font-weight:600;color:var(--ink)}
  .card .role{font-size:5.5px;color:var(--muted)}
  .card-front-dark{top:225px;height:99px}
  .card-front-dark .top{position:absolute;left:0;right:0;top:0;height:46px;background:var(--card-dark);color:#fff;padding:7px 8px;display:flex;justify-content:space-between}
  .card-front-dark .top .name{color:#fff}
  .card-front-dark .top .small{color:#d6d8e0}
  .card .brand{position:absolute;font-size:10px}
  .card .brand-dot{width:10px;height:10px}
  .card .brand-tag{font-size:3.6px}
  .card-front-dark .brand{left:46px;top:52px}
  .card-front-dark .band{height:20px}
  .card-front-light{top:327px;height:93px}
  .card-front-light .top{position:absolute;left:0;right:0;top:0;height:40px;background:linear-gradient(180deg,#f3f4f8,#dfe1e9);padding:6px 8px;display:flex;justify-content:space-between}
  .card-front-light .brand{left:46px;top:46px}
  .card-front-light .band{height:20px}
  .card-white{height:100px}
  .card-white.one{top:451px}
  .card-white.two{top:559px}
  .card-white .address{position:absolute;left:8px;top:8px;width:62px}
  .card-white .person{position:absolute;left:80px;top:8px}
  .card-white .contact{position:absolute;left:80px;top:36px}
  .card-white .band{height:30px;background:linear-gradient(180deg,#fff 0%,var(--brand-soft) 30%,var(--brand) 100%)}
  .card-white .brand{left:60px;bottom:8px;color:#fff}
  .card-white .brand .brand-dot{background:#fff}
</style>
</head>
<body>

  <!-- Business cards -->
  <section class="sheet card card-front-dark">
    <div class="top">
      <div class="small">14 Brindle Works<br>Oakfield Lane<br>Stoneham<br>Wexshire WX7 2QP</div>
      <div><p class="name">Dean Marlow</p><p class="role">Technical Director</p></div>
    </div>
    <div class="brand"><span class="brand-dot"></span><span>Pivotal<span class="brand-tag">Network Services Group</span></span></div>
    <div class="band"></div>
  </section>

  <section class="sheet card card-front-light">
    <div class="top">
      <div class="small">Tel: 01632 960 418<br>dean.marlow@pivotal-nsg.net</div>
      <div><p class="name">Dean Marlow</p><p class="role">Technical Director</p></div>
    </div>
    <div class="brand"><span class="brand-dot"></span><span>Pivotal<span class="brand-tag">Network Services Group</span></span></div>
    <div class="band"></div>
  </section>

  <section class="sheet card card-white one">
    <p class="address small">14 Brindle Works Oakfield Lane Stoneham Wexshire WX7 2QP</p>
    <div class="person"><p class="name">Dean Marlow</p><p class="role">Technical Director</p></div>
    <p class="contact small">Tel: 01632 960 418<br>dean.marlow@pivotal-nsg.net</p>
    <div class="band"></div>
    <div class="brand"><span class="brand-dot"></span><span>Pivotal<span class="brand-tag">Network Services Group</span></span></div>
  </section>

  <section class="sheet card card-white two">
    <p class="address small">14 Brindle Works Oakfield Lane Stoneham Wexshire WX7 2QP</p>
    <div class="person"><p class="name">Dean Marlow</p><p class="role">Technical Director</p></div>
    <p class="contact small">Mob: 07700 900 215<br>dean.marlow@pivotal-nsg.net</p>
    <div class="band"></div>
    <div class="brand"><span class="brand-dot"></span><span>Pivotal<span class="brand-tag">Network Services Group</span></span></div>
  </section>

  <!-- Letterhead -->
  <section class="sheet letterhead">
    <div class="brand"><span class="brand-dot"></span><span>Pivotal<span class="brand-tag">Network Services Group</span></span></div>
    <p class="address">14 Brindle Works<br>Oakfield Lane<br>Stoneham<br>Wexshire<br>WX7 2QP<br><br>Tel: 01632 960 418<br>Email: dean.marlow@pivotal-nsg.net</p>
    <div class="watermark"></div>
    <div class="band"></div>
    <p class="url">www.pivotal-nsg.net</p>
    <span class="corner-dot"></span>
  </section>

  <!-- Envelope front -->
  <section class="sheet envelope-front">
    <div class="brand"><span class="brand-dot"></span><span>Pivotal<span class="brand-tag">Network Services Group</span></span></div>
    <p class="address">14 Brindle Works<br>Oakfield Lane<br>Stoneham<br>Wexshire<br>WX7 2QP</p>
    <div class="band"></div>
    <p class="url">www.pivotal-nsg.net</p>
    <span class="corner-dot"></span>
  </section>

  <!-- Envelope back -->
  <section class="sheet envelope-back">
    <svg width="418" height="177" viewBox="0 0 418 177" aria-hidden="true">
      <defs>
        <linearGradient id="flapFill" x1="0" y1="0" x2="0" y2="1">
          <stop offset="0" stop-color="#3b4bab"/>
          <stop offset="1" stop-color="#1f2c78"/>
        </linearGradient>
      </defs>
      <path d="M0 0 H418 V20 C330 30 260 70 209 82 C158 70 88 30 0 20 Z" fill="url(#flapFill)"/>
      <path d="M0 20 C88 30 158 70 209 82 C260 70 330 30 418 20" fill="none" stroke="#c9cfee" stroke-width="2"/>
    </svg>
    <span class="flap-dot"></span>
  </section>

</body>
</html>
```